" A RB DELTORA fornece soluções personalizadas para a geração de energia fotovoltaica, que é uma fonte sustentável proveniente de recursos limpos, sem emissão de carbono. Somos habilitados a importar e comercializar módulos fotovoltaicos que transformam a radiação solar em energia elétrica através de inversores. Temos equipe qualificada para instalar os equipamentos, atendendo todos os requisitos de segurança exigidos por lei. Os equipamentos têm certificação do Normaq, CE (Conformidade Européia) e OKP (Órgão de Perícia Industrial da Alemanha). "

```html
<!DOCTYPE html>
<html lang="pt-BR">
<head>
<meta charset="utf-8">
<title>RB DELTORA — Envelope</title>
<link href="https://fonts.googleapis.com/css2?family=Montserrat:wght@300;400;500&display=swap" rel="stylesheet">
<style>
  :root{
    --navy:#14224a;
    --navy-soft:#1b2b58;
    --green:#5fb346;
    --paper:#ffffff;
    --ink:#1b2a52;
    --muted:#6c7690;
    --globe:#eef0f3;
    --light-text:#d7ddeb;
    --stage:#e9eaec;
  }
  html,body{margin:0;padding:0;width:1200px;height:1200px;overflow:hidden;background:var(--stage);}
  .canvas{position:relative;width:1200px;height:1200px;}
  .envelope{position:absolute;top:360px;width:384px;height:530px;}
  .envelope--front{left:210px;}
  .envelope--back{left:594px;}
  .envelope svg{display:block;width:384px;height:530px;}
  .brand{font-family:"Montserrat",sans-serif;font-weight:500;fill:var(--ink);}
  .brand--light{fill:#ffffff;}
  .tagline{font-family:"Montserrat",sans-serif;font-weight:300;fill:var(--muted);}
  .tagline--light{fill:#c9d1e4;}
  .contact{font-family:"Montserrat",sans-serif;font-weight:400;fill:var(--light-text);font-size:6.5px;letter-spacing:.4px;}
  .social{font-family:"Montserrat",sans-serif;font-weight:400;fill:var(--light-text);font-size:5.5px;}
</style>
</head>
<body>
<main class="canvas">

  <section class="envelope envelope--front" aria-label="Frente do envelope">
    <svg viewBox="0 0 384 530" xmlns="http://www.w3.org/2000/svg">
      <path class="flap-tab" d="M0 0 L26 0 L14 26 L0 26 Z" fill="var(--green)"/>
      <rect x="0" y="14" width="384" height="516" fill="var(--paper)"/>
      <circle role="img" aria-label="Globo decorativo em tom claro ao fundo" cx="110" cy="250" r="175" fill="var(--globe)" opacity=".8"/>
      <path class="curve-navy" d="M0 455 C120 490 270 440 384 350 L384 530 L0 530 Z" fill="var(--navy)"/>
      <path class="curve-green" d="M0 468 C130 505 280 460 384 372 L384 530 L0 530 Z" fill="var(--green)"/>
      <g class="logo">
        <text class="brand" x="192" y="250" font-size="22" letter-spacing="3" text-anchor="middle">RB DELTORA</text>
        <text class="tagline" x="192" y="265" font-size="7.5" text-anchor="middle">Energia Solar com Eficiência e Cuidado</text>
      </g>
    </svg>
  </section>

  <section class="envelope envelope--back" aria-label="Verso do envelope">
    <svg viewBox="0 0 384 530" xmlns="http://www.w3.org/2000/svg">
      <path class="flap-tab" d="M358 0 L384 0 L384 26 L370 26 Z" fill="var(--green)"/>
      <rect x="0" y="14" width="384" height="516" fill="var(--navy)"/>
      <circle role="img" aria-label="Globo decorativo em tom escuro ao fundo" cx="330" cy="250" r="150" fill="var(--navy-soft)" opacity=".7"/>
      <path class="sweep-green" d="M384 70 C345 270 200 410 0 462 L0 480 C215 440 365 300 384 160 Z" fill="var(--green)"/>
      <path class="sweep-green-thin" d="M384 240 C345 350 235 430 70 480 L105 480 C255 440 360 360 384 285 Z" fill="var(--green)"/>

      <g class="logo">
        <text class="brand brand--light" x="192" y="50" font-size="12" letter-spacing="1.5" text-anchor="middle">RB DELTORA</text>
        <text class="tagline tagline--light" x="192" y="59" font-size="4.6" text-anchor="middle">Energia Solar com Eficiência e Cuidado</text>
      </g>

      <g class="address" transform="translate(125 125)">
        <text class="contact" x="0" y="0">RUA DAS PALMEIRAS, 210</text>
        <text class="contact" x="0" y="16">EDIFÍCIO SOLAR, SALA 12 - CENTRO</text>
        <text class="contact" x="0" y="32">CEP 58000-000 - JOÃO PESSOA - PB - BRASIL</text>
        <text class="contact" x="0" y="48">TEL: (83) 3000-0000 | (83) 3000-0001</text>
      </g>

      <g class="socials" transform="translate(296 448)">
        <circle cx="0" cy="0" r="3.5" fill="var(--light-text)"/>
        <text class="social" x="7" y="2">/rbdeltora</text>
        <circle cx="0" cy="16" r="3.5" fill="var(--light-text)"/>
        <text class="social" x="7" y="18">/rbdeltora</text>
        <circle cx="0" cy="32" r="3.5" fill="var(--light-text)"/>
        <text class="social" x="7" y="34">contato@rbdeltora.com</text>
      </g>
    </svg>
  </section>

</main>
</body>
</html>
```